Design for a 4 screens iOS and Android app - "TrajiMesur"

The app allows you to track your car gasoline refill ...
We need a design for the 4 screens of the app:
a) 1 form with 3 fields.
b) 1 simple list view
c) 1 summary view
d) 1 text page
2 "alerts" items are also to be designed.
No specific guidelines, nor logo or whatever.
It will be a free app distributed on iOS and Androïd.
We just want to make it looking nice & very usable for end users.
Target Market(s)
B2C app
Industry/Entity Type
Android

```html
<!DOCTYPE html>
<html lang="en">
<head>
<meta charset="utf-8">
<title>TrajiMesur – app screens</title>
<link rel="stylesheet" href="https://fonts.googleapis.com/css2?family=Exo+2:wght@400;500;600&display=swap">
<style>
  :root {
    --stage: #e2e4e6;
    --screen-top: #1f4d6d;
    --screen-bottom: #2f7c9a;
    --screen-dark: #213d55;
    --screen-dark-bottom: #29506b;
    --yellow: #ede10b;
    --yellow-dim: #7f7a18;
    --gold: #e9c743;
    --white: #ffffff;
    --white-soft: rgba(255,255,255,0.82);
    --line: rgba(255,255,255,0.45);
    --ink: #24465f;
    --alert-bg: #eef0f2;
  }
  * { box-sizing: border-box; margin: 0; padding: 0; }
  html, body { width: 1200px; height: 800px; overflow: hidden; }
  body {
    background: var(--stage);
    font-family: "Exo 2", "Helvetica Neue", Arial, sans-serif;
    color: var(--white);
    position: relative;
  }
  .screen {
    position: absolute;
    top: 118px;
    width: 270px;
    height: 564px;
    background: linear-gradient(160deg, var(--screen-top), var(--screen-bottom));
    box-shadow: 0 12px 30px rgba(0,0,0,0.22);
    overflow: hidden;
  }
  .screen--list { left: 24px; }
  .screen--alert { left: 318px; background: linear-gradient(160deg, var(--screen-dark), var(--screen-dark-bottom)); }
  .screen--form { left: 612px; }
  .screen--summary { left: 906px; }

  /* status bar */
  .status-bar {
    height: 24px;
    display: flex;
    align-items: center;
    justify-content: space-between;
    padding: 0 10px;
    font-size: 11px;
  }
  .status-bar__signal { display: flex; gap: 2px; align-items: center; }
  .status-bar__signal span { width: 4px; height: 4px; border-radius: 50%; background: var(--white); }
  .status-bar__battery { width: 20px; height: 9px; border: 1px solid var(--white); border-radius: 2px; padding: 1px; }
  .status-bar__battery i { display: block; height: 100%; background: var(--white); }

  /* list */
  .refill-list { list-style: none; padding: 14px 16px 0; }
  .refill {
    display: grid;
    grid-template-columns: 1fr 46px 54px;
    grid-template-rows: 22px 22px;
    height: 66px;
    padding-top: 10px;
    border-bottom: 1px solid rgba(255,255,255,0.1);
    font-size: 13px;
    line-height: 22px;
  }
  .refill__date { grid-column: 1; grid-row: 1; display: flex; align-items: center; gap: 4px; white-space: nowrap; }
  .refill__date svg { width: 11px; height: 11px; flex: none; }
  .refill__km { grid-column: 1; grid-row: 2; white-space: nowrap; }
  .refill__liters { grid-column: 2; grid-row: 2; text-align: right; white-space: nowrap; }
  .refill__price { grid-column: 3; grid-row: 1; text-align: right; color: var(--gold); white-space: nowrap; }
  .pager { position: absolute; bottom: 14px; left: 0; right: 0; display: flex; justify-content: center; gap: 5px; }
  .pager span { width: 5px; height: 5px; border: 1px solid var(--white); border-radius: 50%; }
  .pager span.is-active { background: var(--white); }

  /* form */
  .entry-form { padding: 128px 30px 0; display: flex; flex-direction: column; gap: 14px; }
  .field {
    height: 42px;
    border: 1px solid var(--line);
    border-radius: 21px;
    display: flex;
    align-items: center;
    justify-content: center;
    font-size: 24px;
    font-weight: 500;
  }
  .button-save {
    height: 44px;
    border-radius: 22px;
    background: var(--yellow);
    color: var(--ink);
    display: flex;
    align-items: center;
    justify-content: center;
    font-size: 19px;
  }
  .brand-foot {
    position: absolute;
    bottom: 54px;
    left: 0; right: 0;
    display: flex;
    flex-direction: column;
    align-items: center;
    gap: 8px;
  }
  .brand-foot__mark { display: flex; align-items: center; gap: 8px; font-size: 16px; font-weight: 500; }
  .brand-foot__mark span.dot { width: 18px; height: 18px; border-radius: 50%; background: var(--white); }
  .brand-foot__link { font-size: 18px; }

  /* dimmed form under alert */
  .screen--alert .field { border-color: rgba(255,255,255,0.15); color: rgba(255,255,255,0.3); }
  .screen--alert .button-save { background: var(--yellow-dim); color: rgba(36,70,95,0.8); }
  .screen--alert .brand-foot { opacity: 0.55; }
  .alert {
    position: absolute;
    top: 200px;
    left: 34px;
    width: 202px;
    border-radius: 6px;
    overflow: hidden;
    box-shadow: 0 8px 20px rgba(0,0,0,0.3);
  }
  .alert__message {
    height: 66px;
    background: var(--alert-bg);
    color: var(--ink);
    display: flex; align-items: center; justify-content: center;
    font-size: 24px; font-weight: 500;
  }
  .alert__ok {
    height: 48px;
    background: var(--yellow);
    color: var(--ink);
    display: flex; align-items: center; justify-content: center;
    font-size: 30px; font-weight: 600;
  }

  /* summary */
  .month-list { padding: 40px 16px 0; }
  .month { margin-bottom: 26px; }
  .month__head {
    display: flex; justify-content: space-between; align-items: baseline;
    border-bottom: 1px solid var(--white-soft);
    padding-bottom: 4px; margin-bottom: 6px;
  }
  .month__title { font-size: 22px; color: var(--gold); }
  .month__cost { font-size: 18px; color: var(--gold); }
  .month__row { display: flex; justify-content: space-between; font-size: 17px; line-height: 23px; }
</style>
</head>
<body>

<section class="screen screen--list">
  <div class="status-bar">
    <div class="status-bar__signal"><span></span><span></span><span></span><span></span><span></span></div>
    <span>9:00 AM</span>
    <div class="status-bar__battery"><i></i></div>
  </div>
  <ul class="refill-list">
    <li class="refill"><span class="refill__date">12 févr. 2016 11:07 <svg viewBox="0 0 12 12"><circle cx="6" cy="6" r="5" fill="none" stroke="#fff"/><path d="M6 3v3h2" fill="none" stroke="#fff"/></svg></span><span class="refill__km">127600 km</span><span class="refill__liters">51.07</span><span class="refill__price">48.29€</span></li>
    <li class="refill"><span class="refill__date">15 févr. 2016 14:24 <svg viewBox="0 0 12 12"><circle cx="6" cy="6" r="5" fill="none" stroke="#fff"/><path d="M6 3v3h2" fill="none" stroke="#fff"/></svg></span><span class="refill__km">127500 km</span><span class="refill__liters">49.88</span><span class="refill__price">47.25€</span></li>
    <li class="refill"><span class="refill__date">04 févr. 2016 11:21 <svg viewBox="0 0 12 12"><circle cx="6" cy="6" r="5" fill="none" stroke="#fff"/><path d="M6 3v3h2" fill="none" stroke="#fff"/></svg></span><span class="refill__km">177507 km</span><span class="refill__liters">46.00</span><span class="refill__price">40.10€</span></li>
    <li class="refill"><span class="refill__date">13 févr. 2016 10:14 <svg viewBox="0 0 12 12"><circle cx="6" cy="6" r="5" fill="none" stroke="#fff"/><path d="M6 3v3h2" fill="none" stroke="#fff"/></svg></span><span class="refill__km">177570 km</span><span class="refill__liters">30.07</span><span class="refill__price">57.20€</span></li>
    <li class="refill"><span class="refill__date">17 févr. 2016 12:23 <svg viewBox="0 0 12 12"><circle cx="6" cy="6" r="5" fill="none" stroke="#fff"/><path d="M6 3v3h2" fill="none" stroke="#fff"/></svg></span><span class="refill__km">127880 km</span><span class="refill__liters">42.22</span><span class="refill__price">37.25€</span></li>
    <li class="refill"><span class="refill__date">15 févr. 2016 14:24 <svg viewBox="0 0 12 12"><circle cx="6" cy="6" r="5" fill="none" stroke="#fff"/><path d="M6 3v3h2" fill="none" stroke="#fff"/></svg></span><span class="refill__km">127500 km</span><span class="refill__liters">49.88</span><span class="refill__price">47.25€</span></li>
    <li class="refill"><span class="refill__date">15 févr. 2016 14:24 <svg viewBox="0 0 12 12"><circle cx="6" cy="6" r="5" fill="none" stroke="#fff"/><path d="M6 3v3h2" fill="none" stroke="#fff"/></svg></span><span class="refill__km">127570 km</span><span class="refill__liters">40.24</span><span class="refill__price">43.21€</span></li>
  </ul>
  <div class="pager"><span class="is-active"></span><span></span><span></span></div>
</section>

<section class="screen screen--alert">
  <div class="status-bar">
    <div class="status-bar__signal"><span></span><span></span><span></span><span></span><span></span></div>
    <span>9:00 AM</span>
    <div class="status-bar__battery"><i></i></div>
  </div>
  <div class="entry-form">
    <div class="field">10257</div>
    <div class="field">Liters</div>
    <div class="field">Price</div>
    <div class="button-save">Save results</div>
  </div>
  <div class="alert" role="alertdialog">
    <div class="alert__message">Data saved</div>
    <div class="alert__ok">OK</div>
  </div>
  <div class="brand-foot">
    <div class="brand-foot__mark"><span class="dot"></span>TrajiMesur</div>
    <div class="brand-foot__link">About us</div>
  </div>
</section>

<section class="screen screen--form">
  <div class="status-bar">
    <div class="status-bar__signal"><span></span><span></span><span></span><span></span><span></span></div>
    <span>9:00 AM</span>
    <div class="status-bar__battery"><i></i></div>
  </div>
  <div class="entry-form">
    <div class="field">10257</div>
    <div class="field">Liters</div>
    <div class="field">Price</div>
    <div class="button-save">Save results</div>
  </div>
  <div class="brand-foot">
    <div class="brand-foot__mark"><span class="dot"></span>TrajiMesur</div>
    <div class="brand-foot__link">About us</div>
  </div>
</section>

<section class="screen screen--summary">
  <div class="status-bar">
    <div class="status-bar__signal"><span></span><span></span><span></span><span></span><span></span></div>
    <span>9:00 AM</span>
    <div class="status-bar__battery"><i></i></div>
  </div>
  <div class="month-list">
    <article class="month">
      <div class="month__head"><span class="month__title">février 2016</span><span class="month__cost">570.54€</span></div>
      <div class="month__row"><span>Total cost</span><span>7500 km</span></div>
      <div class="month__row"><span>Mileage</span><span>11</span></div>
      <div class="month__row"><span>Full tanks</span><span>6.5</span></div>
      <div class="month__row"><span>Consumption</span><span></span></div>
    </article>
    <article class="month">
      <div class="month__head"><span class="month__title">janvier 2016</span><span class="month__cost">570.54€</span></div>
      <div class="month__row"><span>Total cost</span><span>7500 km</span></div>
      <div class="month__row"><span>Mileage</span><span>11</span></div>
      <div class="month__row"><span>Full tanks</span><span>6.5</span></div>
      <div class="month__row"><span>Consumption</span><span></span></div>
    </article>
    <article class="month">
      <div class="month__head"><span class="month__title">décembre 2016</span><span class="month__cost">570.54€</span></div>
      <div class="month__row"><span>Total cost</span><span>7500 km</span></div>
      <div class="month__row"><span>Mileage</span><span>11</span></div>
      <div class="month__row"><span>Full tanks</span><span>6.5</span></div>
      <div class="month__row"><span>Consumption</span><span></span></div>
    </article>
  </div>
</section>

</body>
</html>
```